Modern Label for Loose Tea pouches on 4.5x6 Label

We need a new label for our teas that is very simple in design, but stylish and modern. This will be used to print labels for our loose tea pouches. The label will be at max 4.5x6 inches in size. There should be a place for the tea name, description, ingredients, and size that is changeable.
Preferably an AI file that allows me to setup variables to change the above items. There will also need to be our logo which is supplied, and our address on the label.
Address:
Brindle Teas
148 Lower Ferncliff Lane
Highland, NY 12097
Target Market(s)
Tea Lovers
Requirements
Must have
- Adobe Illustrator file with variables setup for replacement of tea name, description, ingredients, and size (weights 2oz, 4oz, 8oz, 1lb)

```html
<!DOCTYPE html>
<html lang="en">
<head>
<meta charset="utf-8">
<title>Brindle Teas – Loose Tea Label</title>
<link rel="stylesheet" href="https://fonts.googleapis.com/css2?family=Source+Sans+3:wght@400;600;700&display=swap">
<style>
  :root {
    --bg-deep: #140002;
    --bg-mid: #240407;
    --panel: #c8c8c9;
    --ink: #231f20;
    --white: #ffffff;
    --brand-pink: #d9529f;
    --brand-green: #b3cf2b;
    --photo-warm: #b4553a;
    --photo-light: #dcdcdd;
  }
  * { margin: 0; padding: 0; box-sizing: border-box; }
  html, body { width: 900px; height: 1200px; overflow: hidden; background: var(--bg-deep); }
  .label {
    position: relative;
    width: 900px;
    height: 1200px;
    overflow: hidden;
    background: radial-gradient(ellipse at 50% 45%, var(--bg-mid) 0%, var(--bg-deep) 75%);
    font-family: "Source Sans 3", sans-serif;
    color: var(--ink);
  }
  .brand {
    position: absolute;
    left: 0; top: 60px;
    width: 900px;
    text-align: center;
  }
  .brand-mark {
    display: block;
    width: 150px; height: 150px;
    margin: 0 auto 70px;
    border-radius: 50%;
    background: var(--brand-pink);
  }
  .brand-name {
    font-size: 68px;
    font-weight: 700;
    letter-spacing: 2px;
    line-height: 1;
    color: var(--brand-green);
  }
  .info-panel {
    position: absolute;
    left: 208px; top: 406px;
    width: 484px; height: 690px;
    background: var(--panel);
  }
  .description { text-align: center; padding-top: 14px; }
  .section-title { font-weight: 400; font-size: 30px; line-height: 1.2; }
  .description p {
    font-size: 19px;
    line-height: 27px;
    letter-spacing: -0.3px;
  }
  .product-photo {
    position: absolute;
    left: 16px; top: 126px;
    width: 452px; height: 392px;
    background: radial-gradient(ellipse at 50% 50%, var(--photo-warm) 0%, var(--photo-light) 60%, var(--panel) 100%);
  }
  .ingredients {
    position: absolute;
    left: 29px; top: 518px;
    width: 431px;
  }
  .ingredients .section-title { font-size: 32px; margin-bottom: 0; }
  .ingredients .line {
    display: block;
    font-size: 20.5px;
    line-height: 26.5px;
    text-align: justify;
    text-align-last: justify;
  }
  .address {
    position: absolute;
    left: 180px; top: 1102px;
    width: 540px;
    text-align: center;
    color: var(--white);
  }
  .address .company { font-size: 29px; line-height: 1.2; }
  .address .street { font-size: 22.5px; line-height: 1.3; }
  .weight {
    position: absolute;
    left: 730px; top: 1080px;
    width: 142px;
    text-align: center;
    color: var(--white);
  }
  .weight .weight-label { font-size: 29px; font-weight: 700; line-height: 1.1; }
  .weight .weight-value { font-size: 64px; font-weight: 400; line-height: 1; }
</style>
</head>
<body>
  <main class="label">
    <header class="brand">
      <span class="brand-mark" aria-hidden="true"></span>
      <h1 class="brand-name">BRINDLE TEAS</h1>
    </header>

    <section class="info-panel">
      <div class="description">
        <h2 class="section-title">Description</h2>
        <p>Lorem ipsum dolor sit amet, consectetuer adipiscing elit.<br>Aenean commodo ligula eget dolor. Aenean massa</p>
      </div>
      <div class="product-photo" role="img" aria-label="Photo of a glass cup of red tea on a saucer with fresh green tea leaves"></div>
      <div class="ingredients">
        <h2 class="section-title">Ingredients:</h2>
        <p>
          <span class="line">Lorem ipsum dolor sit amet, consectetuer</span>
          <span class="line">adipiscing elit. Aenean commodo ligula eget</span>
          <span class="line">dolor. Aenean massa. Cum sociis natoque</span>
          <span class="line">penatibus et magnis dis parturient montes,</span>
        </p>
      </div>
    </section>

    <footer class="address">
      <p class="company">Brindle Teas,</p>
      <p class="street">148 Lower Ferncliff Lane, Highland, NY 12097</p>
    </footer>

    <div class="weight">
      <p class="weight-label">weights</p>
      <p class="weight-value">2oz</p>
    </div>
  </main>
</body>
</html>
```